Business Cards, Letterheads, Envelopes

A company's new identity to be reflected on its stationery items

Target Market(s)

Large Corporate Companies & Enterprises

Font styles to use
Sans Serif

Colors
0555a3
3176b5
85abd2
85cae6
33a6d7
0293ce

```html
<!DOCTYPE html>
<html lang="en">
<head>
<meta charset="utf-8">
<title>Orlivane Systems – Business Card</title>
<link rel="stylesheet" href="https://fonts.googleapis.com/css2?family=Roboto:wght@400;500&display=swap">
<style>
  :root {
    --brand-blue: #3a8ac9;
    --brand-blue-dark: #3176b5;
    --text-dark: #4a4a4a;
    --text-grey: #9a9a9a;
    --card-white: #ffffff;
    --page-bg: #ececec;
    --divider: #b8b8b8;
  }
  * { margin: 0; padding: 0; box-sizing: border-box; }
  html, body {
    width: 1125px; height: 1200px; overflow: hidden;
    background: var(--page-bg);
    font-family: "Roboto", Arial, sans-serif;
  }
  .canvas { position: relative; width: 1125px; height: 1200px; }
  .card {
    position: absolute; left: 166px; width: 800px; height: 457px;
    box-shadow: 0 2px 6px rgba(0,0,0,0.18);
  }
  .card-front { top: 103px; background: var(--card-white); }
  .card-back { top: 620px; background: var(--brand-blue); }

  .brand {
    position: absolute; left: 100px; top: 200px;
    display: flex; align-items: center; gap: 16px;
  }
  .brand-dot { width: 30px; height: 30px; border-radius: 50%; background: var(--brand-blue); }
  .brand-name {
    font-weight: 500; font-size: 20px; line-height: 24px;
    letter-spacing: 2px; text-transform: uppercase; color: var(--brand-blue);
  }

  .divider {
    position: absolute; left: 432px; top: 105px; width: 2px; height: 255px;
    background: linear-gradient(to bottom, rgba(184,184,184,0), var(--divider) 25%, var(--divider) 75%, rgba(184,184,184,0));
  }

  .contact { position: absolute; left: 470px; top: 110px; color: var(--text-dark); }
  .person-name { font-weight: 500; font-size: 30px; color: var(--brand-blue); line-height: 36px; }
  .person-title { font-weight: 500; font-size: 20px; color: var(--text-grey); line-height: 24px; margin-bottom: 14px; }
  .address { font-size: 19px; line-height: 24px; margin-bottom: 14px; }
  .contact-list { list-style: none; font-size: 19px; line-height: 24px; }
  .contact-list li { display: flex; align-items: center; gap: 12px; }
  .contact-list svg { width: 20px; height: 20px; fill: var(--brand-blue); flex: none; }

  .web-band {
    position: absolute; left: 0; top: 385px; width: 800px; height: 35px;
    background: var(--brand-blue);
    color: #fff; font-size: 19px; letter-spacing: 5px;
    display: flex; align-items: center; justify-content: center;
  }

  .back-lockup {
    position: absolute; right: 48px; top: 306px; text-align: left; color: #fff;
  }
  .back-name {
    font-weight: 500; font-size: 22px; line-height: 26px; letter-spacing: 2px;
    text-transform: uppercase; padding-bottom: 6px;
    border-bottom: 1px solid rgba(255,255,255,0.7);
  }
  .back-web { font-size: 19px; letter-spacing: 3.5px; margin-top: 10px; }
</style>
</head>
<body>
<div class="canvas">
  <section class="card card-front">
    <div class="brand">
      <div class="brand-dot"></div>
      <div class="brand-name">Orlivane Systems<br>Private Limited</div>
    </div>
    <div class="divider"></div>
    <div class="contact">
      <div class="person-name">Daniel Harper</div>
      <div class="person-title">President</div>
      <div class="address">2140 Alder Ridge Road<br>Halden Falls, Alaska 34512</div>
      <ul class="contact-list">
        <li><svg viewBox="0 0 24 24"><path d="M6.6 10.8a15.2 15.2 0 0 0 6.6 6.6l2.2-2.2a1 1 0 0 1 1-.25 11.4 11.4 0 0 0 3.6.57 1 1 0 0 1 1 1V20a1 1 0 0 1-1 1A17 17 0 0 1 3 4a1 1 0 0 1 1-1h3.5a1 1 0 0 1 1 1 11.4 11.4 0 0 0 .57 3.6 1 1 0 0 1-.25 1z"/></svg>555-214-0386</li>
        <li><svg viewBox="0 0 24 24"><path d="M7 1h10a2 2 0 0 1 2 2v18a2 2 0 0 1-2 2H7a2 2 0 0 1-2-2V3a2 2 0 0 1 2-2zm0 3v14h10V4zm5 15.5a1 1 0 1 0 0 2 1 1 0 0 0 0-2z"/></svg>555-730-4152</li>
        <li><svg viewBox="0 0 24 24"><path d="M7 2h10v6H7zM3 9h18a1 1 0 0 1 1 1v8h-4v-3H6v3H2v-8a1 1 0 0 1 1-1zm4 7h10v6H7z"/></svg>555-468-2971</li>
        <li><svg viewBox="0 0 24 24"><path d="M3 6h18v12H3zm1.5 1.5v.4L12 13l7.5-5.1v-.4z"/></svg>harper@orlivanesys.com</li>
      </ul>
    </div>
    <div class="web-band">www.orlivanesys.com</div>
  </section>

  <section class="card card-back">
    <div class="back-lockup">
      <div class="back-name">Orlivane Systems<br>Private Limited</div>
      <div class="back-web">www.orlivanesys.com</div>
    </div>
  </section>
</div>
</body>
</html>
```